Core Values Poster for Technology Business

A core values poster for our office. We don't have much in mind beyond a couple of logos (we have two companies) and then the 4 Core Values we want to present. Mostly, we want this to be simple (easy to take in as a reminder in 5-10 seconds) in a very visually appealing way.

If you can incorporate a high-look-and-feel, great, but not if it over complicates the entire poster/sign.

The core values are:
Relationships Matter
Passion Drives us to Excellence
All About Teamwork
Consistent, Resourceful, Relentless

Our file with both logos together is attached. This is a low-res version. We would provide a high-res version for final production.

Industry/Entity Type

Business

Font styles to use
Serif

Colors
ec1f27
0255a3

Requirements
Nice to have
• This is an update. To be able to incorporate some of our corporate look-and-feel, but not have a black background (as on our kovaline.com stie), please see the Video Conferencing Slick file that I have uploaded. Might be able to use parts of this type of format to tie in (but not use it exactly as-is - since this is a client facing document).

```html
<!DOCTYPE html>
<html lang="en">
<head>
<meta charset="utf-8">
<title>Core Values</title>
<link rel="stylesheet" href="https://fonts.googleapis.com/css2?family=Questrial&family=Roboto+Slab:wght@400;800&display=swap">
<style>
  :root {
    --ink: #3a3a3c;
    --brand-blue: #0255a3;
    --brand-red: #ec1f27;
    --sky: #8fb3d9;
    --sky-text: #8bb0dc;
    --blush: #f48b91;
    --blush-text: #f6a8ac;
    --paper: #ffffff;
  }
  html, body {
    margin: 0;
    padding: 0;
    width: 1200px;
    height: 943px;
    overflow: hidden;
    background: var(--paper);
  }
  .poster {
    display: block;
    width: 1200px;
    height: 943px;
  }
  .headline {
    font-family: "Questrial", sans-serif;
    font-size: 222px;
    fill: var(--ink);
  }
  .sans { font-family: "Questrial", sans-serif; }
  .slab { font-family: "Roboto Slab", serif; }
  .bold { font-weight: 800; }
  .regular { font-weight: 400; }

  .band-relationships { fill: var(--brand-blue); }
  .band-passion { fill: var(--blush); }
  .band-teamwork { fill: var(--sky); }
  .band-consistent { fill: var(--brand-red); }

  .on-white { fill: var(--paper); }
  .on-sky { fill: var(--sky-text); }
  .on-red { fill: var(--brand-red); }
  .on-blue { fill: var(--brand-blue); }
  .on-blush { fill: var(--blush-text); }
</style>
</head>
<body>
<svg class="poster" viewBox="0 0 1200 943" xmlns="http://www.w3.org/2000/svg" role="img" aria-label="Core Values: Relationships matter; Passion drives us to Excellence; All About Teamwork; Consistent, Resourceful, Relentless">
  <text class="headline" x="-5" y="170" textLength="1160" lengthAdjust="spacingAndGlyphs">Core Values</text>

  <g class="value value-relationships">
    <rect class="band-relationships" x="291" y="199" width="866" height="150"/>
    <text class="slab bold on-sky" x="394" y="291" font-size="111" textLength="759" lengthAdjust="spacingAndGlyphs">Relationships</text>
    <text class="slab bold on-white" x="733" y="351" font-size="60" textLength="238" lengthAdjust="spacingAndGlyphs">matter</text>
  </g>

  <g class="value value-passion">
    <rect class="band-passion" x="35" y="386" width="866" height="150"/>
    <text class="slab bold on-white" x="53" y="457" font-size="100" textLength="425" lengthAdjust="spacingAndGlyphs">Passion</text>
    <text class="slab regular on-red" x="497" y="457" font-size="57" textLength="394" lengthAdjust="spacingAndGlyphs">drives us to</text>
    <text class="slab bold on-white" x="368" y="540" font-size="80" textLength="497" lengthAdjust="spacingAndGlyphs">Excellence</text>
  </g>

  <g class="value value-teamwork">
    <rect class="band-teamwork" x="222" y="575" width="866" height="151"/>
    <text class="slab regular on-blue" x="540" y="658" font-size="62" textLength="326" lengthAdjust="spacingAndGlyphs">All About</text>
    <text class="slab bold on-white" x="360" y="730" font-size="106" textLength="580" lengthAdjust="spacingAndGlyphs">Teamwork</text>
  </g>

  <g class="value value-consistent">
    <rect class="band-consistent" x="97" y="762" width="926" height="150"/>
    <text class="sans on-white" x="196" y="830" font-size="95" textLength="571" lengthAdjust="spacingAndGlyphs">Consistent,</text>
    <text class="slab bold on-blush" x="106" y="894" font-size="64" textLength="500" lengthAdjust="spacingAndGlyphs">Resourceful,</text>
    <text class="slab bold on-white" x="614" y="915" font-size="64" textLength="410" lengthAdjust="spacingAndGlyphs">Relentless</text>
  </g>
</svg>
</body>
</html>
```